Coach/consultant in conflict and challenge needs an enticing flyer

I need a double sided DL flyer design that will describe my work in helping people meet conflict and emotional challenge so they can learn and grow from these difficulties. I want to give a flavour of my style through fresh colours, repeated images used differently (the spiral), and a sense of positivity around conflict and difficulty. I want to attract people who are keen to do things differently and want to engage with creative processes rather than getting stuck in familiar patterns. My work is creative and often includes use of story, images and fables, so I want to convey that as well. I also place the work in a spiritual context, but grounded in practicality so I don't want it to seem New Age or flakey. I want something that seems innovative, professional and intriguing. I've included a sample of something I mocked up in word and also a copy of a flyer for Marla Quennet's Ember Gathering that inspired me to get a DL flyer. I want the design to communicate trust and transformation and engaging with fresh ways of doing things by moving past old habits

Target Market(s)

Mid 30s plus women and men who want to change their approach to conflict and emotional difficulties and are willing to take the creative and challenging journey to do that

Industry/Entity Type

Learn

Colors
acd136
00a990

Requirements
Must have
• a shift in the use of the spiral image,
• use of image of me (Norah)
• bright fresh colours olours that represent growth and transformation--I've suggested lime green as it suggests a sense of growth
• easy to read text
Nice to have
• Interesting non-traditional fonts perhaps text in a contemporary sans serif and another brush script font (like the Ember Gathering example)
• bleed to the edge and run off the page images or text
Should not have
• anything that represents too much tradition or stuckness

```html
<!DOCTYPE html>
<html lang="en">
<head>
<meta charset="utf-8">
<title>Norah Pellham — Coach, Educator and Mediator</title>
<link href="https://fonts.googleapis.com/css2?family=Figtree:ital,wght@0,400;0,500;1,400&family=Bungee&display=swap" rel="stylesheet">
<style>
  :root {
    --lime: #a0cd32;
    --lime-edge: #8cc63f;
    --hex-line: #97cb3a;
    --earth: #5b4636;
    --ink: #1f1f1f;
    --mist-1: #ffffff;
    --mist-2: #e6f1ee;
    --mist-3: #cfe4df;
  }
  * { box-sizing: border-box; margin: 0; padding: 0; }
  html, body { width: 1200px; height: 600px; overflow: hidden; background: #fff; }
  .flyer {
    position: relative;
    width: 1200px;
    height: 600px;
    overflow: hidden;
    font-family: "Figtree", sans-serif;
  }
  .flyer__mist {
    position: absolute;
    inset: 0 602px 0 0;
    background:
      radial-gradient(ellipse 60% 40% at 80% 5%, var(--mist-3), transparent 70%),
      radial-gradient(ellipse 50% 30% at 95% 95%, var(--mist-2), transparent 70%),
      linear-gradient(150deg, var(--mist-1) 0%, var(--mist-2) 45%, var(--mist-1) 70%, var(--mist-2) 100%);
  }
  .flyer__gallery {
    position: absolute;
    left: 0;
    top: 0;
    width: 600px;
    height: 600px;
  }
  .flyer__edge {
    position: absolute;
    left: 598px;
    top: 0;
    width: 12px;
    height: 600px;
    background: var(--lime-edge);
  }
  .flyer__notches {
    position: absolute;
    left: 598px;
    top: 0;
  }
  .flyer__panel {
    position: absolute;
    left: 608px;
    top: 0;
    right: 0;
    bottom: 0;
    background: var(--lime);
  }
  .brand {
    position: absolute;
    left: 24px;
    top: 58px;
    display: flex;
    align-items: center;
    gap: 26px;
  }
  .brand__mark {
    width: 94px;
    height: 94px;
    border-radius: 50%;
    background: var(--earth);
    flex: none;
  }
  .brand__name {
    font-family: "Figtree", sans-serif;
    font-weight: 500;
    font-size: 56px;
    line-height: 1;
    color: var(--earth);
    letter-spacing: -0.5px;
  }
  .values {
    position: absolute;
    left: 26px;
    top: 210px;
    width: 542px;
    display: flex;
    justify-content: space-between;
    font-family: "Bungee", sans-serif;
    font-size: 22px;
    line-height: 30px;
    color: var(--earth);
    white-space: nowrap;
  }
  .intro, .bio {
    position: absolute;
    left: 26px;
    width: 526px;
    font-size: 21px;
    line-height: 32px;
    color: var(--ink);
  }
  .intro { top: 296px; }
  .bio { top: 438px; width: 540px; font-style: italic; }
</style>
</head>
<body>
<main class="flyer">
  <div class="flyer__mist"></div>

  <svg class="flyer__gallery" viewBox="0 0 750 750">
    <defs>
      <linearGradient id="tone-climb" x1="0" y1="0" x2="1" y2="1">
        <stop offset="0" stop-color="#8a8a8a"/>
        <stop offset="0.6" stop-color="#c9c9c9"/>
        <stop offset="1" stop-color="#3a3a3a"/>
      </linearGradient>
      <linearGradient id="tone-listen" x1="0" y1="0" x2="1" y2="0">
        <stop offset="0" stop-color="#cfcfcf"/>
        <stop offset="0.5" stop-color="#8f8f8f"/>
        <stop offset="1" stop-color="#bdbdbd"/>
      </linearGradient>
      <radialGradient id="tone-idea" cx="0.5" cy="0.55" r="0.6">
        <stop offset="0" stop-color="#f2dc3a"/>
        <stop offset="0.25" stop-color="#f7f3d8"/>
        <stop offset="1" stop-color="#e4e4e4"/>
      </radialGradient>
    </defs>

    <g class="hex-frames" fill="none" stroke="var(--hex-line)" stroke-width="4">
      <polygon points="382,97 515,174 515,324 382,401 249,324 249,174"/>
      <polygon points="184,340 318,417 318,568 184,645 50,568 50,417"/>
      <polygon points="571,340 705,417 705,568 571,645 437,568 437,417"/>
    </g>

    <g class="accent-bars" stroke="var(--hex-line)" stroke-width="9" stroke-linecap="butt">
      <line x1="230" y1="155" x2="360" y2="80"/>
      <line x1="198" y1="326" x2="330" y2="402"/>
      <line x1="424" y1="402" x2="555" y2="326"/>
      <line x1="40" y1="590" x2="172" y2="666"/>
      <line x1="586" y1="662" x2="716" y2="588"/>
    </g>

    <polygon class="photo photo--climb" role="img" aria-label="Black and white photo of a rock climber on a cliff face"
      points="232,262 455,120 462,372" fill="url(#tone-climb)"/>
    <polygon class="photo photo--listen" role="img" aria-label="Black and white photo of a smiling woman listening in a group"
      points="87,370 318,505 95,630" fill="url(#tone-listen)"/>
    <polygon class="photo photo--idea" role="img" aria-label="Crumpled yellow paper forming a glowing light bulb"
      points="570,343 450,590 705,590" fill="url(#tone-idea)"/>
  </svg>

  <div class="flyer__edge"></div>
  <svg class="flyer__notches" width="12" height="600" viewBox="0 0 12 600" aria-hidden="true">
    <polygon points="0,204 9,212 0,220" fill="#fff"/>
    <polygon points="0,384 9,392 0,400" fill="#fff"/>
  </svg>

  <section class="flyer__panel">
    <header class="brand">
      <span class="brand__mark" aria-hidden="true"></span>
      <h1 class="brand__name">Norah Pellham</h1>
    </header>

    <p class="values">
      <span># courage</span>
      <span># listening</span>
      <span># creativity</span>
    </p>

    <p class="intro">Challenge, change and conflict are a natural part of life. When we greet them with courage, and listen to what they tell us, we grow in wisdom, resilience and creativity.</p>

    <p class="bio">Norah Pellham is a coach, educator and mediator. She works with people who want to harvest the fruits of challenge and conflict so they live life differently.</p>
  </section>
</main>
</body>
</html>
```